Strong, modern, clean Business Card design

Looking for a stunning, but CLEAN business card design. While we are a faith-based organization, we do NOT want this to look religious.

Industry/Entity Type

Non-Profit

Contact Information for Business Card

Dale Munroe | Lead Pastor
dale@BrightHarvestHope.org
406-555-0148
PO Box 7316
Alder Creek, MT 80571

Font styles to use
Serif
Sans Serif

Requirements
Should not have
• Religious imagery or symbolism

```html
<!DOCTYPE html>
<html lang="en">
<head>
<meta charset="UTF-8">
<title>Harvest Hope Church – Business Card</title>
<link rel="stylesheet" href="https://fonts.googleapis.com/css2?family=Cinzel:wght@500&family=Libre+Baskerville:wght@700&family=Lato:wght@400&display=swap">
<style>
  :root {
    --bg: #1c1c1e;
    --card: #131315;
    --accent: #4f7f9b;
    --text: #ecedee;
    --rule: #2c2c30;
  }
  * { margin: 0; padding: 0; box-sizing: border-box; }
  html, body { width: 1200px; height: 900px; overflow: hidden; background: var(--bg); }
  .canvas {
    width: 1200px; height: 900px;
    display: flex; flex-direction: column; align-items: center; justify-content: center; gap: 56px;
  }
  .card {
    position: relative;
    width: 560px; height: 320px;
    background: var(--card);
    border-radius: 22px;
    box-shadow: 0 14px 36px rgba(0,0,0,.55);
  }
  /* back side */
  .card--back { display: flex; align-items: center; justify-content: center; }
  .brand-square {
    width: 132px; height: 118px;
    background: var(--accent);
    border-radius: 22px;
  }
  .brand-name {
    font-family: "Cinzel", serif; font-weight: 500;
    color: var(--accent); font-size: 24px; letter-spacing: 2px; line-height: 1.1;
  }
  /* front side */
  .brand-lockup {
    position: absolute; top: 36px; left: 0; right: 0;
    display: flex; align-items: center; justify-content: center; gap: 14px;
  }
  .brand-lockup .brand-square { width: 96px; height: 84px; border-radius: 16px; }
  .rule {
    position: absolute; left: 160px; right: 44px; top: 146px;
    height: 1px; background: var(--rule);
  }
  .address {
    position: absolute; right: 44px; top: 170px;
    font-family: "Lato", sans-serif; font-style: normal; color: var(--text);
    font-size: 15px; line-height: 1.35; text-align: right;
  }
  .person { position: absolute; left: 44px; bottom: 34px; }
  .person-name {
    font-family: "Libre Baskerville", serif; font-weight: 700;
    color: var(--accent); font-size: 17px; letter-spacing: .5px; text-transform: uppercase;
  }
  .person-title {
    font-family: "Lato", sans-serif; color: var(--text); font-size: 15px; margin-bottom: 14px;
  }
  .contact-list { list-style: none; font-family: "Lato", sans-serif; color: var(--text); font-size: 15px; }
  .contact-list li { display: flex; align-items: center; gap: 9px; line-height: 1.5; }
  .contact-icon { width: 13px; height: 13px; fill: var(--accent); flex: none; }
</style>
</head>
<body>
<main class="canvas">
  <section class="card card--back" aria-label="Card back">
    <div class="brand-square"></div>
  </section>

  <section class="card card--front" aria-label="Card front">
    <div class="brand-lockup">
      <div class="brand-square"></div>
      <div class="brand-name">Harvest Hope Church</div>
    </div>
    <div class="rule"></div>
    <address class="address">PO Box 7316<br>Alder Creek, MT 80571</address>
    <div class="person">
      <div class="person-name">Dale Munroe</div>
      <div class="person-title">Lead Pastor</div>
      <ul class="contact-list">
        <li>
          <svg class="contact-icon" viewBox="0 0 16 16" aria-hidden="true"><path d="M3.6 1.5l2.3 2.8-1.4 1.6c.9 2 2.5 3.6 4.6 4.6l1.6-1.4 2.8 2.3-1.3 2.1C6.7 13.3 2.7 9.3 1.5 3z"/></svg>
          406-555-0148
        </li>
        <li>
          <svg class="contact-icon" viewBox="0 0 16 16" aria-hidden="true"><path d="M1 3h14v10H1z M2.5 4.5L8 8.6l5.5-4.1" stroke="#131315" stroke-width="1.2"/></svg>
          dale@BrightHarvestHope.org
        </li>
      </ul>
    </div>
  </section>
</main>
</body>
</html>
```